R7M Meridian Business Card Design

We need a business card created for our New Business "R7M Meridian"<br/><br/>The business card design is up to you however the following information must be on the business card:<br/><br/>Front of the business card -<br/>Email :dorianv@r7mmeridian.nz<br/>Mobile: +64 (0) 22 4871 659<br/>Website: www.r7mmeridian.nz<br/>Card Owner Name: Dorian Valcourt<br/>Company Title: Business Development Manager<br/>Slogan: "The FINEST of two shores". <br/>Logo On the front attached to the design brief<br/><br/>On the back: <br/>Space on the back for 4 more versions of the logo across the bottom of the card indicating different subsidiary brands - R7M Coffee, R7M Arts, R7M ?? (The card will be used for all of these brands - We Will add the extra subsidiary logos to the design once the design is finished (We are a graphics design team). <br/><br/>Other than that we want a premium feeling logo that remains universally usable depending on the business entity that we are using the card for. The use of bright bold colours would be great but we still want the card to feel premium.
Target Market(s)
Gift Design and Manufacturing Companies
Contact Information for Business Card
Front of the business card -
Email :dorianv@r7mmeridian.nz
Mobile: +64 (0) 22 4871 659
Website: www.r7mmeridian.nz
Card Owner Name: Dorian Valcourt
Company Title: Business Development Manager
Slogan: "The FINEST of two shores".
Logo On the front attached to the design brief

```html
<!DOCTYPE html>
<html lang="en">
<head>
<meta charset="utf-8">
<title>R7M Meridian Business Card</title>
<link rel="stylesheet" href="https://fonts.googleapis.com/css2?family=Michroma&family=Open+Sans:wght@400;600;700&display=swap">
<style>
  :root {
    --stage: #2b2b2b;
    --card-black: #161616;
    --card-black-light: #2a2a2a;
    --card-white: #ffffff;
    --brand-blue: #2f3b9c;
    --ink: #3a3a3a;
    --band: #1a1a1a;
    --silver: #a8a8a8;
    --watermark: #eceef6;
    --on-dark: #ffffff;
  }
  * { box-sizing: border-box; margin: 0; padding: 0; }
  html, body { width: 1200px; height: 900px; overflow: hidden; }
  body {
    background: var(--stage);
    font-family: "Open Sans", Arial, sans-serif;
    position: relative;
  }
  .card {
    position: absolute;
    left: 250px;
    width: 700px;
    height: 400px;
    border-radius: 24px;
    overflow: hidden;
  }
  /* Back of card */
  .card-back {
    top: 30px;
    background: radial-gradient(ellipse at 60% 40%, var(--card-black-light), var(--card-black) 70%);
  }
  .back-brand {
    position: absolute;
    top: 130px;
    left: 0; right: 0;
    text-align: center;
    font-size: 54px;
    font-weight: 700;
    color: var(--silver);
    letter-spacing: 1px;
  }
  .back-slogan {
    position: absolute;
    top: 300px;
    left: 0; right: 0;
    text-align: center;
    font-size: 19px;
    color: var(--on-dark);
    letter-spacing: 0.5px;
  }
  .back-slogan svg { vertical-align: middle; margin: 0 10px; }
  .back-slogan strong { font-weight: 700; }

  /* Front of card */
  .card-front {
    top: 470px;
    background: var(--card-white);
  }
  .accent-bar {
    position: absolute;
    left: 0; top: 26px;
    width: 18px; height: 64px;
    background: var(--band);
  }
  .holder-name {
    position: absolute;
    left: 40px; top: 28px;
    font-family: "Michroma", "Arial Black", sans-serif;
    font-size: 28px;
    font-weight: 400;
    color: var(--brand-blue);
    letter-spacing: 2px;
    text-transform: uppercase;
    -webkit-text-stroke: 1.2px var(--brand-blue);
  }
  .holder-title {
    position: absolute;
    left: 40px; top: 72px;
    font-size: 18px;
    color: var(--ink);
    letter-spacing: 0.5px;
  }
  .brand-watermark {
    position: absolute;
    right: 36px; top: 140px;
    font-size: 60px;
    font-weight: 700;
    color: var(--watermark);
  }
  .front-slogan {
    position: absolute;
    right: 40px; top: 212px;
    font-size: 22px;
    color: var(--brand-blue);
  }
  .front-slogan strong { font-weight: 700; }
  .contact-band {
    position: absolute;
    left: 180px; right: 0;
    top: 258px; height: 108px;
    background: var(--band);
    border-radius: 54px 0 0 54px;
  }
  .front-brand {
    position: absolute;
    left: 28px; top: 290px;
    display: flex;
    align-items: center;
    gap: 10px;
    background: var(--card-white);
    padding: 10px 16px 10px 6px;
    border-radius: 0 40px 40px 0;
    font-size: 24px;
    font-weight: 700;
    color: var(--brand-blue);
  }
  .brand-dot {
    width: 16px; height: 16px;
    border-radius: 50%;
    background: var(--brand-blue);
  }
  .contact-list {
    position: absolute;
    left: 440px; top: 272px;
    list-style: none;
    color: var(--on-dark);
    font-size: 18px;
    line-height: 27px;
  }
  .contact-list li { display: flex; align-items: center; gap: 10px; }
  .contact-list svg { flex: none; }
</style>
</head>
<body>

<section class="card card-back" aria-label="Card back">
  <div class="back-brand">R7M Meridian</div>
  <p class="back-slogan">
    <svg width="12" height="12" viewBox="0 0 12 12"><polygon points="12,0 12,12 0,6" fill="#fff"/></svg>The <strong>FINEST</strong> of two shores<svg width="12" height="12" viewBox="0 0 12 12"><polygon points="0,0 0,12 12,6" fill="#fff"/></svg>
  </p>
</section>

<section class="card card-front" aria-label="Card front">
  <div class="accent-bar"></div>
  <h1 class="holder-name">Dorian Valcourt</h1>
  <p class="holder-title">Business Development Manager</p>
  <div class="brand-watermark" aria-hidden="true">R7M Meridian</div>
  <p class="front-slogan">The <strong>FINEST</strong> of two shores</p>
  <div class="contact-band"></div>
  <div class="front-brand"><span class="brand-dot"></span>R7M Meridian</div>
  <ul class="contact-list">
    <li>
      <svg width="16" height="16" viewBox="0 0 24 24"><path d="M6.6 10.8a15 15 0 0 0 6.6 6.6l2.2-2.2a1 1 0 0 1 1-.25 11.4 11.4 0 0 0 3.6.6 1 1 0 0 1 1 1V20a1 1 0 0 1-1 1A17 17 0 0 1 3 4a1 1 0 0 1 1-1h3.5a1 1 0 0 1 1 1c0 1.25.2 2.45.6 3.6a1 1 0 0 1-.25 1z" fill="#fff"/></svg>
      +64 (0) 22 4871 659
    </li>
    <li>
      <svg width="16" height="16" viewBox="0 0 24 24"><rect x="2.5" y="5" width="19" height="14" rx="1.5" fill="none" stroke="#fff" stroke-width="2"/><path d="M3 6l9 7 9-7" fill="none" stroke="#fff" stroke-width="2"/></svg>
      dorianv@r7mmeridian.nz
    </li>
    <li>
      <svg width="16" height="16" viewBox="0 0 24 24"><circle cx="12" cy="12" r="9.5" fill="none" stroke="#fff" stroke-width="2"/><ellipse cx="12" cy="12" rx="4" ry="9.5" fill="none" stroke="#fff" stroke-width="2"/><path d="M2.5 12h19" stroke="#fff" stroke-width="2"/></svg>
      www.r7mmeridian.nz
    </li>
  </ul>
</section>

</body>
</html>
```